New Townhome community needs for sale sign.

need a 4 foot by 8 foot banner to put on building listing newly constructed townhomes as "coming soon" to market. Construction is scheduled to be completed Dec 2024. Sale of units will begin Spring of 2025.
6 individual townhome units each 2,000 square feet. each unit is 3 bedroom 2.5 bathroom with 2 car garage and each has a rooftop "sky lounge" with amazing views. Gated community. Units available for sale Spring of 2025. Real estate company selling units will be KLM & Partners. Will need KLM & Partners Logo on the banner. Would like to keep with the same blue color scheme as the KLM & Partners logo. phone number on banner to be 602-555-4179. web klmpartnersx.com.

```html
<!DOCTYPE html>
<html lang="en">
<head>
<meta charset="utf-8">
<title>Coming Soon – Townhome Banner</title>
<link href="https://fonts.googleapis.com/css2?family=Montserrat:wght@400;500;700;800&display=swap" rel="stylesheet">
<style>
  :root {
    --sky-blue: #29a3d6;
    --deep-blue: #1f6fa0;
    --ink: #333333;
    --white: #ffffff;
    --page: #eef1f4;
    --photo-dark: #1c1c1e;
    --photo-mid: #4a4440;
  }
  * { box-sizing: border-box; margin: 0; padding: 0; }
  html, body {
    width: 1200px; height: 818px; overflow: hidden;
    background: var(--page);
    font-family: "Montserrat", sans-serif;
  }
  .banner {
    position: absolute; left: 20px; top: 119px;
    width: 1160px; height: 580px;
    background: var(--white);
    overflow: hidden;
  }
  .hero-photo {
    position: absolute; left: 0; top: 0; width: 100%; height: 274px;
    background: linear-gradient(100deg, var(--photo-dark) 0%, var(--photo-mid) 45%, #2b2826 70%, var(--photo-dark) 100%);
  }
  .corner-mark {
    position: absolute; width: 94px; height: 80px;
  }
  .corner-mark--top { left: 15px; top: 21px; }
  .corner-mark--bottom { left: 1102px; top: 540px; width: 48px; height: 40px; }
  .headline {
    position: absolute; left: 89px; top: 40px;
    font-weight: 800; font-size: 112px; line-height: 1.1;
    color: var(--white); letter-spacing: -1px;
  }
  .headline .dots { color: var(--sky-blue); }
  .feature {
    position: absolute; width: 352px;
    display: flex; align-items: center;
    padding: 0 40px 0 26px;
    font-weight: 700; font-size: 20px; line-height: 1.2;
    color: var(--white); text-transform: uppercase;
    clip-path: polygon(0 0, 86% 0, 100% 48%, 100% 100%, 0 100%);
  }
  .feature--light { background: var(--sky-blue); top: 214px; height: 96px; }
  .feature--dark { background: var(--deep-blue); top: 317px; height: 96px; }
  .col-1 { left: 40px; }
  .col-2 { left: 403px; }
  .col-3 { left: 767px; }
  .brand {
    position: absolute; left: 42px; top: 462px;
    display: flex; align-items: center; gap: 18px;
  }
  .brand-square { width: 70px; height: 70px; background: var(--sky-blue); }
  .brand-name {
    font-weight: 700; font-size: 50px; color: var(--ink); letter-spacing: -0.5px;
  }
  .divider {
    position: absolute; left: 579px; top: 449px;
    width: 3px; height: 104px; background: var(--sky-blue);
  }
  .contact {
    position: absolute; left: 604px; top: 432px; width: 516px;
    display: flex; flex-direction: column; align-items: center;
  }
  .phone {
    font-weight: 800; font-size: 68px; line-height: 1.1; color: var(--ink); letter-spacing: -1px;
  }
  .web {
    display: flex; align-items: center; gap: 8px; width: 100%;
    font-weight: 500; font-size: 46px; line-height: 1.1; color: var(--deep-blue);
  }
  .web::before, .web::after {
    content: ""; flex: 1; height: 2px; background: var(--ink);
  }
</style>
</head>
<body>
  <main class="banner">
    <div class="hero-photo" role="img" aria-label="Photo of a real estate agent shaking hands with a smiling couple in a home"></div>
    <svg class="corner-mark corner-mark--top" viewBox="0 0 94 80" aria-hidden="true"><polygon points="0,0 94,0 47,80" fill="var(--sky-blue)"/></svg>
    <h1 class="headline">Coming Soon<span class="dots">...</span></h1>

    <div class="feature feature--light col-1">6 Individual Townhome Units Each 2,000 Square Feet</div>
    <div class="feature feature--light col-2">Each Unit is 3 Bedroom 2.5 Bathroom with 2 Car Garage</div>
    <div class="feature feature--light col-3">Each has a Rooftop "Sky Lounge" with Amazing Views</div>
    <div class="feature feature--dark col-1">Gated Community</div>
    <div class="feature feature--dark col-2">Units Available for Sale Spring of 2025</div>
    <div class="feature feature--dark col-3">Real Estate Company Selling Units will be KLM &amp; Partners</div>

    <div class="brand">
      <span class="brand-square"></span>
      <span class="brand-name">KLM &amp; Partners</span>
    </div>
    <div class="divider"></div>
    <div class="contact">
      <div class="phone">602-555-4179</div>
      <div class="web">klmpartnersx.com</div>
    </div>
    <svg class="corner-mark corner-mark--bottom" viewBox="0 0 48 40" aria-hidden="true"><polygon points="24,0 48,40 0,40" fill="var(--sky-blue)"/></svg>
  </main>
</body>
</html>
```